Tandle Design Prize - $10,000 tablet app design contest, Retail Catalogue Category

Tandle is a marketplace for Slatex App Templates (similar to PageLoom templates). We want you to design an app template for sale in our marketplace which targets Retail Catalogue Apps (Slatex Apps that are created for Product Catalogues. For example: paint, clothing… etc).

It’s up to you to create pages or features for the App Template that you think are appropriate. Creativity will be rewarded! Here are some example pages or features that you could create:

• Welcome page
• Features
• Product pages
• Product details
• Share products on Friendvale
• Maps – store locations or events
• Social media integration
• Animations and video

Your design should be Vibrant, Engaging and Contemporary. If you have an Slatex, download Tandle Viewer and download template examples in the download tab.

Your entry must include:
• A brief description of your template
• Preview images of all pages of your template

Attached to this project are free templates to help you get started with your design. We have included:
1. A free portfolio template for designers/photographers
2. Icons and artwork to use in your template
3. Blank pages template
4. Form template
5. Video ad template

If you are selected as a finalist you will be required to submit an .oproject file containing:
• Your InDesign source files
• Preview images of your template
• All creative / stock assets used in the template (animations, video etc.)
• A text file with instructions on how to update the template
• A metadata .txt file containing template details and your information

How to enter:
1. Register at Marketplace and view the instructions under the welcome message https://marketplace.tandlebase.com/welcome
2. Download Tandle Editor: https://support.tandlebase.com/entries/58140926-tandle-editor
3. Use the free templates provided in this brief to create your designs and submit to ArtHarbor

Reason: Due to the Christmas break we are extending the deadline of our competition. Thank you for time and effort - I will be providing feedback over the next couple of days! Best wishes, Melodie

Hi All,

I have received many screenshots with some great designs! I just wanted to clarify that you are designing Tandle app templates including Tandle features and not just page designs?

Read Hints for Newcomer Tandlers to guide you through the template creation process

Before you start designing templates for Tandle Marketplace

·       Read the Quality Standards

·       Read the Copyright Information 

·       Use the Template Quality Checklist to ensure your template follows our guidelines. 

What should my project file contain?

·       A folder containing your source files, e.g. InDesign. This must be named Source.

·       The Tandle content files. This must be named Bundle.

·       Instructions, explaining to a customer how to use your template.

Best wishes,

Melodie

Reason: We are extending the competition by 7 days to give you more time!

Reason: Due to the lack of submissions to this category we are extending the deadline by 10 days Please let us know if you would like further information on this contest. Best wishes, Melodie

Target Market(s)

Entrepreneurs who wish to create Slatex Apps by using our App design templates.

Industry/Entity Type

Store

Requirements
Must have
• You will need Tandle Editor to open the .oproject files attached to this brief. Get it here: https://support.tandlebase.com/entries/58140926-tandle-editor
Should not have
• • Low quality, fuzzy or blurry images
• Any stock images or content which you do not own the rights to
• Any material which could be considered inappropriate or offensive

```html
<!DOCTYPE html>
<html lang="en">
<head>
<meta charset="utf-8">
<title>NO.23 Vintage Wine – Product Detail</title>
<link rel="stylesheet" href="https://fonts.googleapis.com/css2?family=Lobster&family=Source+Sans+3:wght@400;600&family=Ubuntu:wght@500&display=swap">
<style>
  :root {
    --bg-deep: #15100c;
    --bg-wood: #3d3026;
    --bg-wood-light: #4c3d30;
    --panel: #a88a66;
    --panel-light: #b39672;
    --panel-dark: #94765a;
    --ink: #15110d;
    --cart-top: #cf3d45;
    --cart-bottom: #a8242d;
    --cart-text: #6a1419;
    --more-top: #e67826;
    --more-bottom: #c8560f;
    --more-text: #6d2a06;
  }
  * { box-sizing: border-box; margin: 0; padding: 0; }
  html, body { width: 1200px; height: 900px; overflow: hidden; }
  body { background: var(--bg-deep); }

  .screen {
    position: relative;
    width: 1200px;
    height: 900px;
    overflow: hidden;
    background: radial-gradient(ellipse at 50% 45%, var(--bg-wood-light) 0%, var(--bg-wood) 45%, var(--bg-deep) 100%);
  }

  .shelf-bottle {
    position: absolute;
    width: 78px;
    border-radius: 18px 18px 10px 10px;
    box-shadow: 0 6px 14px rgba(0,0,0,.5);
  }
  .shelf-bottle.top { top: 68px; height: 200px; }
  .shelf-bottle.bottom { top: 640px; height: 201px; border-radius: 10px; }

  .bottle-pale    { background: linear-gradient(90deg, #9ea08a, #d6d8c2 45%, #a7a991); }
  .bottle-rose    { background: linear-gradient(90deg, #7e3322, #c4603f 45%, #8a3826); }
  .bottle-black   { background: linear-gradient(90deg, #0c0c0c, #2e2e2e 45%, #101010); }
  .bottle-olive   { background: linear-gradient(90deg, #8d8f3c, #c3c66a 45%, #8f9240); }
  .bottle-green   { background: linear-gradient(90deg, #121a0d, #34452a 45%, #141c0f); }
  .bottle-amber   { background: linear-gradient(90deg, #141208, #363323 45%, #15130a); }
  .bottle-claret  { background: linear-gradient(90deg, #170a0c, #44222a 45%, #180b0d); }
  .bottle-clear   { background: linear-gradient(90deg, #a9b19f, #dfe5d5 45%, #aeb6a4); }

  .detail-panel {
    position: absolute;
    left: 103px;
    top: 213px;
    width: 996px;
    height: 463px;
    border-radius: 7px;
    background: radial-gradient(ellipse at 60% 40%, var(--panel-light) 0%, var(--panel) 55%, var(--panel-dark) 100%);
    box-shadow: 0 8px 22px rgba(0,0,0,.55);
  }

  .featured-bottle {
    position: absolute;
    left: 176px;
    top: 84px;
    width: 178px;
    height: 668px;
    border-radius: 40px 40px 22px 22px;
    background: linear-gradient(90deg, #150406 0%, #5a0f1c 25%, #a3202e 45%, #5a0f1c 70%, #120305 100%);
    box-shadow: 0 12px 28px rgba(0,0,0,.6);
    z-index: 2;
  }

  .product-info {
    position: absolute;
    left: 429px;
    top: 236px;
    width: 640px;
    color: var(--ink);
    z-index: 3;
  }
  .product-title {
    font-family: "Lobster", cursive;
    font-weight: 400;
    font-size: 66px;
    line-height: 1;
    letter-spacing: .5px;
  }
  .product-meta {
    margin-top: 14px;
    font-family: "Source Sans 3", sans-serif;
    font-size: 26px;
    line-height: 1.2;
  }
  .product-meta span + span { margin-left: 10px; }
  .product-description {
    margin-top: 28px;
    width: 620px;
    font-family: "Source Sans 3", sans-serif;
    font-size: 27.5px;
    line-height: 34px;
  }

  .actions {
    position: absolute;
    left: 431px;
    top: 586px;
    display: flex;
    gap: 24px;
    z-index: 3;
  }
  .action-button {
    width: 286px;
    height: 59px;
    border-radius: 6px;
    display: flex;
    align-items: center;
    justify-content: center;
    font-family: "Ubuntu", sans-serif;
    font-weight: 500;
    font-size: 28px;
    box-shadow: 0 2px 4px rgba(0,0,0,.35), inset 0 1px 0 rgba(255,255,255,.25);
  }
  .action-button.add-to-cart {
    background: linear-gradient(var(--cart-top), var(--cart-bottom));
    color: var(--cart-text);
  }
  .action-button.more-like-this {
    background: linear-gradient(var(--more-top), var(--more-bottom));
    color: var(--more-text);
  }
</style>
</head>
<body>
<main class="screen">
  <div class="shelf-bottle top bottle-pale" style="left:115px" role="img" aria-label="White wine bottle on the shelf"></div>
  <div class="shelf-bottle top bottle-rose" style="left:404px" role="img" aria-label="Rosé wine bottle on the shelf"></div>
  <div class="shelf-bottle top bottle-black" style="left:717px" role="img" aria-label="Dark red wine bottle on the shelf"></div>
  <div class="shelf-bottle top bottle-olive" style="left:1010px" role="img" aria-label="Green-gold white wine bottle on the shelf"></div>

  <div class="shelf-bottle bottom bottle-green" style="left:108px" role="img" aria-label="Sauvignon blanc bottle with green label"></div>
  <div class="shelf-bottle bottom bottle-amber" style="left:408px" role="img" aria-label="Sauvignon blanc bottle with yellow label"></div>
  <div class="shelf-bottle bottom bottle-claret" style="left:704px" role="img" aria-label="Chardonnay bottle with red label"></div>
  <div class="shelf-bottle bottom bottle-clear" style="left:1010px" role="img" aria-label="Clear white wine bottle"></div>

  <section class="detail-panel" aria-label="Product details"></section>

  <div class="featured-bottle" role="img" aria-label="Featured red Chardonnay bottle with decorative vintage wine label"></div>

  <div class="product-info">
    <h1 class="product-title">NO.23 Vintage Wine</h1>
    <p class="product-meta"><span>Category: Chardonnay</span><span>Year: 2003</span></p>
    <p class="product-description">Dolor sit amet, consectetuer adipiscing elit. Aenean commodo ligula eget dolor. Aenean massa. Fum sociis natoque penati-bus et magnis dis parturient montes.</p>
  </div>

  <div class="actions">
    <div class="action-button add-to-cart">add to cart</div>
    <div class="action-button more-like-this">more like this</div>
  </div>
</main>
</body>
</html>
```